New Company Letterhead

Hi All

We are looking for a fresh new letterhead. At present we have rolling colour behind our logo but would like one flat colour. See attached for examples of our current letterhead, logos and company colour chart. All information currently contained within the letterhead (i.e. address, ABN, tel, fax, email etc) needs to still be included in the new letterhead. Preferred font is Helvetica or something similar.

Any queries please shout.

Many thanks & best of luck,

Rosalind Pemberton
Marbury Estate Agents

Hi Designers Great work so far! Would it be possible to add to your designs the phrase; Done. Different. Preferably in a light grey? Many thanks, Ros

Industry/Entity Type

It Company

```html
<!DOCTYPE html>
<html lang="en">
<head>
<meta charset="utf-8">
<title>Marbury Estate Agents – Letterhead Concepts</title>
<link href="https://fonts.googleapis.com/css2?family=Arimo:wght@400;700&display=swap" rel="stylesheet">
<style>
  :root {
    --brand-blue: #3572a0;
    --sidebar-grey: #adadb0;
    --paper: #ffffff;
    --ink: #111111;
    --icon: #222222;
    --backdrop: #e8e4df;
  }
  * { margin: 0; padding: 0; box-sizing: border-box; }
  html, body { width: 1200px; height: 1000px; overflow: hidden; }
  body {
    background: var(--backdrop);
    font-family: "Arimo", Helvetica, Arial, sans-serif;
    position: relative;
  }
  .sheet {
    position: absolute;
    top: 86px;
    width: 500px;
    height: 852px;
    background: var(--paper);
    overflow: hidden;
    box-shadow: 0 2px 8px rgba(0,0,0,0.18);
  }
  .sheet--curves { left: 55px; }
  .sheet--sidebar { left: 659px; }

  .company-name {
    position: absolute;
    color: var(--brand-blue);
    font-weight: 700;
    line-height: 1;
    white-space: nowrap;
  }
  .sheet--curves .company-name { left: 0; right: 0; top: 34px; text-align: center; font-size: 28px; }
  .sheet--sidebar .company-name { left: 10px; top: 44px; font-size: 24px; }

  .sample-label {
    position: absolute;
    color: var(--brand-blue);
    font-weight: 700;
    font-size: 54px;
    white-space: nowrap;
  }
  .sheet--curves .sample-label { left: 110px; top: 404px; }
  .sheet--sidebar .sample-label { left: 200px; top: 410px; }

  .header-swoosh, .footer-arc { position: absolute; left: 0; }
  .header-swoosh { top: 0; }
  .footer-arc { bottom: 0; }

  .contact-item {
    position: absolute;
    transform: translateX(-50%);
    display: flex;
    flex-direction: column;
    align-items: center;
    color: var(--brand-blue);
    font-weight: 700;
    font-size: 13px;
    line-height: 1.1;
    text-align: center;
    white-space: nowrap;
  }
  .contact-item svg { margin-bottom: 4px; }
  .contact-item--phone { left: 52px; top: 742px; }
  .contact-item--fax   { left: 155px; top: 742px; }
  .contact-item--email { left: 287px; top: 735px; }
  .contact-item--web   { left: 440px; top: 730px; }

  .sidebar {
    position: absolute; left: 0; top: 100px; width: 151px; bottom: 0;
    background: var(--sidebar-grey);
  }
  .sidebar__cap { height: 23px; background: var(--brand-blue); }
  .sidebar-tag {
    position: absolute; left: 8px; width: 149px; height: 29px;
  }
  .sidebar-tag svg { position: absolute; left: 0; top: 0; }
  .sidebar-tag__label {
    position: absolute; left: 42px; top: 7px;
    color: var(--paper); font-weight: 700; font-size: 14px; letter-spacing: 1.5px;
  }
  .sidebar-value {
    position: absolute; left: 0; width: 151px;
    text-align: center; color: var(--ink); font-weight: 700; font-size: 14px; line-height: 1.05;
  }
</style>
</head>
<body>

<section class="sheet sheet--curves">
  <svg class="header-swoosh" width="500" height="200" viewBox="0 0 500 200">
    <path d="M0,68 Q250,147 500,70 L500,186 Q250,73 0,189 Z" fill="var(--brand-blue)"/>
  </svg>
  <p class="company-name">Marbury Estate Agents</p>

  <p class="sample-label">Sample 1</p>

  <div class="contact-item contact-item--phone">
    <svg width="22" height="28" viewBox="0 0 22 28"><path d="M8,2 L12,9 L9,11 Q10,17 14,21 L17,19 L21,25 L17,27 Q6,24 3,8 Z" fill="var(--icon)"/></svg>
    <span>(02) 5550 1288</span>
  </div>
  <div class="contact-item contact-item--fax">
    <svg width="26" height="24" viewBox="0 0 26 24"><rect x="6" y="1" width="14" height="8" fill="none" stroke="var(--icon)" stroke-width="2"/><rect x="2" y="10" width="22" height="11" fill="none" stroke="var(--icon)" stroke-width="2"/><line x1="6" y1="15" x2="20" y2="15" stroke="var(--icon)" stroke-width="2"/></svg>
    <span>(02) 5550 1287</span>
  </div>
  <div class="contact-item contact-item--email">
    <svg width="30" height="22" viewBox="0 0 30 22"><rect x="1" y="1" width="28" height="20" fill="none" stroke="var(--icon)" stroke-width="2"/><path d="M1,1 L15,13 L29,1 M1,21 L11,10 M29,21 L19,10" fill="none" stroke="var(--icon)" stroke-width="2"/></svg>
    <span>management@marbury<br>estateagents.com.au</span>
  </div>
  <div class="contact-item contact-item--web">
    <svg width="26" height="26" viewBox="0 0 28 28"><circle cx="14" cy="14" r="12" fill="var(--icon)"/><path d="M7,8 Q12,6 13,11 Q10,14 12,18 Q8,17 6,12 Z M16,5 Q22,7 23,13 Q19,12 17,9 Z M17,17 Q21,17 21,21 Q18,22 17,17 Z" fill="#fff"/></svg>
    <span>www.marburyestate<br>agents.com.au</span>
  </div>

  <svg class="footer-arc" width="500" height="40" viewBox="0 0 500 40">
    <path d="M35,40 Q250,-25 470,40 Z" fill="var(--brand-blue)"/>
  </svg>
</section>

<section class="sheet sheet--sidebar">
  <p class="company-name">Marbury Estate Agents</p>

  <aside class="sidebar">
    <div class="sidebar__cap"></div>
  </aside>

  <div class="sidebar-tag" style="top:220px">
    <svg width="149" height="29" viewBox="0 0 149 29"><path d="M6,0 H149 V29 H6 L0,14.5 Z" fill="var(--brand-blue)"/><path d="M18,6 L22,12 L19,14 Q20,19 23,22 L20,26 Q12,20 14,7 Z" fill="#fff"/></svg>
    <span class="sidebar-tag__label" style="left:26px">PHONE</span>
  </div>
  <p class="sidebar-value" style="top:268px">(02) 5550 1288</p>

  <div class="sidebar-tag" style="top:338px">
    <svg width="149" height="29" viewBox="0 0 149 29"><path d="M6,0 H149 V29 H6 L0,14.5 Z" fill="var(--brand-blue)"/><rect x="15" y="3" width="14" height="8" fill="#fff"/><rect x="11" y="13" width="22" height="12" fill="#fff"/><line x1="14" y1="18" x2="30" y2="18" stroke="var(--brand-blue)" stroke-width="2"/></svg>
    <span class="sidebar-tag__label">FAX</span>
  </div>
  <p class="sidebar-value" style="top:388px">(02) 5550 1287</p>

  <div class="sidebar-tag" style="top:471px">
    <svg width="149" height="29" viewBox="0 0 149 29"><path d="M6,0 H149 V29 H6 L0,14.5 Z" fill="var(--brand-blue)"/><rect x="11" y="4" width="28" height="21" fill="#fff"/><path d="M12,5 L25,16 L38,5 M12,24 L21,14 M38,24 L29,14" fill="none" stroke="var(--brand-blue)" stroke-width="2.5"/></svg>
    <span class="sidebar-tag__label" style="left:45px">E-MAIL</span>
  </div>
  <p class="sidebar-value" style="top:525px;font-size:13px">management@marbury<br>estateagents.com.au</p>

  <div class="sidebar-tag" style="top:594px">
    <svg width="149" height="29" viewBox="0 0 149 29"><path d="M6,0 H149 V29 H6 L0,14.5 Z" fill="var(--brand-blue)"/><circle cx="22" cy="14.5" r="12" fill="#fff"/><path d="M15,8 Q20,7 21,12 Q18,15 20,20 Q15,18 14,13 Z M24,5 Q30,8 31,13 Q26,12 25,9 Z" fill="var(--brand-blue)"/></svg>
    <span class="sidebar-tag__label">WEBSITE</span>
  </div>
  <p class="sidebar-value" style="top:642px">www.marburyestate<br>agents.com.au</p>

  <p class="sample-label">Sample 2</p>
</section>

</body>
</html>
```